Stationery Design Project for Marketing Consultancy

I have started a new consultancy business and require the following elements to be designed using existing logo:
• Business card
• Letterhead
• Envelope (DL, C4, C5)
• Microsoft word template for report writing
• A4 Presentation Folder
• Powerpoint template
COPY FOR FRONT AND BACK OF BUSINESS CARD
logo
'Countable Growth. Bold Outcomes' slogan (but no need to use existing lockup with logo)
name, B Bus. Mktg, Grad Dip Digital Mktg, CPM (post nominal abbreviations in smaller font)
mobile: 04XX-XXX-XXX (I will give details to the winner to add)
website: www.quorvale.com.au
email: info@quorvale.com.au
COPY FOR LETTERHEAD
Logo
Company Name
Please, submit your designs that include business card, letterhead and envelope. Once selected the winner will be asked to complete the project by creating the rest of the artwork.
FINAL FILES
Print ready files to be supplied as well as Indesign files so that minor amends can be made if necessary in future.
• Layered vectors in EPS & PDF
• Screen quality JPEG & PNGs
ABOUT THE BUSINESS: QUORVALE
I work with clients to understand their business challenges, developing and executing Countable Growth strategies tied to key business metrics. Services include:
Services include:
• Business planning and business development
• Marketing and brand strategy
• Insight-driven integrated campaigns
• Loyalty programs and retention marketing
• Marketing automation
• Direct marketing (traditional and digital)
• Content strategy and development
Hi everyone,
Target Market(s)
Corporate decision makers (heads of marketing, general managers etc) and small to medium sized business owners. Predominately male aged 35+
Industry/Entity Type
Marketing
Requirements
Must have
- BRAND PERSONALITY
The successful design will communicate brand personality. I am a professional, results-driven entrepreneur, but want to show off my creative flair.
MEMORABILITY
Looking for a unique and eye-catching design. Am considering special printing effects (die cuts, letterpress, interactive elements, embossing, foiling etc) or a striking minimalist approach.
Nice to have
- I have a mission that could be incorporated on reverse if room -
Turning insights into actions & passion into profit.
Should not have
- Use of pink or green.

```html
<!DOCTYPE html>
<html lang="en">
<head>
<meta charset="utf-8">
<title>Quorvale Business Card</title>
<link rel="stylesheet" href="https://fonts.googleapis.com/css2?family=Montserrat:ital,wght@0,400;0,700;1,400&display=swap">
<style>
  :root {
    --backdrop: #e4e2e0;
    --card-white: #fbfbfa;
    --card-grey: #8d8c98;
    --ink-grey: #5f5e6b;
    --ink-soft: #7a7986;
    --rule: #c9c8cf;
    --accent: #f09a2c;
    --emboss: #a9a8b4;
  }
  * { box-sizing: border-box; margin: 0; padding: 0; }
  html, body {
    width: 1200px; height: 832px; overflow: hidden;
    background: var(--backdrop);
    font-family: "Montserrat", sans-serif;
  }
  .stage {
    position: relative; width: 1200px; height: 832px;
    display: flex; align-items: center; justify-content: center; gap: 60px;
  }
  .card {
    position: relative; width: 510px; height: 292px;
    border-radius: 3px;
    box-shadow: 0 10px 28px rgba(0,0,0,0.18);
  }
  .card--front { background: var(--card-white); }
  .card--back { background: var(--card-grey); }

  .brand {
    position: absolute; top: 44px; left: 0; right: 0;
    display: flex; flex-direction: column; align-items: center; gap: 12px;
  }
  .brand__dot {
    width: 46px; height: 46px; border-radius: 50%; background: var(--ink-soft);
  }
  .brand__name {
    font-weight: 700; font-size: 30px; letter-spacing: 1px; color: var(--ink-grey);
  }

  .person {
    position: absolute; top: 162px; left: 0; right: 0; text-align: center;
  }
  .person__name {
    font-weight: 700; font-size: 14px; letter-spacing: 0.5px; color: var(--ink-grey);
  }
  .person__title {
    font-style: italic; font-size: 11px; color: var(--ink-soft); margin-top: 3px;
  }

  .divider {
    position: absolute; left: 34px; right: 34px; top: 214px;
    height: 1px; background: var(--rule);
  }
  .contacts {
    position: absolute; left: 34px; right: 34px; top: 232px;
    display: flex; justify-content: space-between; list-style: none;
  }
  .contact {
    display: flex; align-items: center; gap: 6px;
    font-size: 11px; color: var(--ink-soft);
  }
  .contact svg { width: 12px; height: 12px; flex: none; }

  .back-mark {
    position: absolute; right: 40px; top: 104px; text-align: right;
  }
  .back-mark__name {
    font-weight: 700; font-size: 48px; letter-spacing: 1px; color: var(--emboss); line-height: 1;
  }
  .back-mark__tagline {
    font-size: 15px; letter-spacing: 2px; text-transform: uppercase;
    color: var(--emboss); margin-top: 6px;
  }
</style>
</head>
<body>
<main class="stage">
  <section class="card card--front" aria-label="Business card front">
    <div class="brand">
      <span class="brand__dot"></span>
      <span class="brand__name">QUORVALE</span>
    </div>
    <div class="person">
      <p class="person__name">DANA WHITLOW</p>
      <p class="person__title">Managing Director</p>
    </div>
    <div class="divider"></div>
    <ul class="contacts">
      <li class="contact">
        <svg viewBox="0 0 12 12" aria-hidden="true"><rect x="3" y="0.5" width="6" height="11" rx="1.2" fill="none" stroke="var(--accent)" stroke-width="1.2"/><circle cx="6" cy="9.5" r="0.7" fill="var(--accent)"/></svg>
        +0491-570-006
      </li>
      <li class="contact">
        <svg viewBox="0 0 12 12" aria-hidden="true"><rect x="0.5" y="2.5" width="11" height="7" fill="var(--accent)"/><path d="M0.5 2.5 L6 6.5 L11.5 2.5" fill="none" stroke="#fff" stroke-width="0.9"/></svg>
        info@quorvale.com.au
      </li>
      <li class="contact">
        <svg viewBox="0 0 12 12" aria-hidden="true"><circle cx="6" cy="6" r="5.3" fill="var(--accent)"/><path d="M0.8 6 H11.2 M6 0.7 C3.5 3.5 3.5 8.5 6 11.3 M6 0.7 C8.5 3.5 8.5 8.5 6 11.3" fill="none" stroke="#fff" stroke-width="0.8"/></svg>
        www.quorvale.com.au
      </li>
    </ul>
  </section>

  <section class="card card--back" aria-label="Business card back">
    <div class="back-mark">
      <p class="back-mark__name">QUORVALE</p>
      <p class="back-mark__tagline">Countable Growth</p>
    </div>
  </section>
</main>
</body>
</html>
```